Clinic for cellulit and fat removal

Name of clinic :
Lumera
- Body & Health (this has to be written on the site.)
I need CMS for me to be able to make changes myself.
A webpage for woman searching for a solution to remove fat and cellulit.
The owner is a brazilian woman in Denmark, and want her sense of aestetic shines thru the website.
There needs to be a slide show on the landing page showing big sliding pictures, of the clinic and and the treatments.
The Cryolipolysis, is a treatment freezing fat and cellulit, and this treatment will be the Attraction of the clinic.
Needs These pages in a horisontal fasion. (written in Danish)
Lumera
Behandlinger
- Cryolipolysis
- Silkora
- Lymfemassage
- Tandrelia
- Copper Tide
Produkter
Priser
Kontakt

```html
<!DOCTYPE html>
<html lang="da">
<head>
<meta charset="utf-8">
<title>Lumera – Body &amp; Health</title>
<link href="https://fonts.googleapis.com/css2?family=Open+Sans:wght@400;600&family=Pacifico&display=swap" rel="stylesheet">
<style>
  :root {
    --sidebar-bg: #ffffff;
    --ink: #1f1f1f;
    --mint: #e0fbf0;
    --teal: #7fcfae;
    --divider: #b9e6d5;
    --brand-pink: #c2347e;
    --hero-light: #f3ece6;
    --hero-warm: #d7ad88;
    --hero-dark: #5a4a42;
    --white: #ffffff;
  }
  * { margin: 0; padding: 0; box-sizing: border-box; }
  html, body { width: 1200px; height: 675px; overflow: hidden; }
  body { font-family: "Open Sans", sans-serif; color: var(--ink); position: relative; background: var(--sidebar-bg); }

  .sidebar { position: absolute; left: 0; top: 0; width: 200px; height: 675px; background: var(--sidebar-bg); }
  .brand { position: absolute; left: 34px; top: 34px; display: flex; align-items: center; gap: 10px; }
  .brand-dot { width: 14px; height: 14px; border-radius: 50%; background: var(--teal); }
  .brand-name { font-size: 28px; font-weight: 400; color: var(--ink); line-height: 1; }
  .brand-tagline { position: absolute; left: 58px; top: 74px; font-size: 12px; color: var(--brand-pink); }

  .main-nav { position: absolute; left: 0; top: 137px; width: 200px; list-style: none; }
  .main-nav li { height: 47px; display: flex; align-items: center; padding-left: 30px; font-size: 11px; border-bottom: 1px dotted var(--divider); }
  .main-nav li.active { background: var(--mint); border-right: 2px solid var(--teal); border-bottom: none; height: 46px; }

  .social { position: absolute; left: 34px; top: 616px; display: flex; align-items: center; gap: 15px; }
  .social span { width: 8px; height: 8px; border-radius: 50%; background: var(--teal); margin: 0 6px; }
  .social span.active { width: 28px; height: 28px; margin: 0; }

  .hero { position: absolute; left: 200px; top: 0; width: 1000px; height: 675px; }
  .hero-photo { position: absolute; inset: 0;
    background:
      radial-gradient(ellipse 45% 40% at 88% 45%, var(--hero-light) 0%, rgba(243,236,230,0) 100%),
      linear-gradient(160deg, #ecdccd 0%, var(--hero-warm) 45%, #c99c77 70%, var(--hero-dark) 100%); }
  .hero-title { position: absolute; left: 58px; top: 190px; font-family: "Pacifico", cursive; color: var(--white); font-size: 80px; line-height: 0.98; font-weight: 400; }
  .hero-title .line-2 { display: block; padding-left: 74px; }
  .hero-button { position: absolute; left: 199px; top: 417px; width: 75px; height: 31px; border: 1px solid var(--white); border-radius: 3px; color: var(--white); font-size: 10px; font-weight: 600; display: flex; align-items: center; justify-content: center; }
  .copyright { position: absolute; right: 21px; top: 632px; font-size: 9px; color: var(--ink); }
</style>
</head>
<body>
  <aside class="sidebar">
    <div class="brand">
      <span class="brand-dot"></span>
      <span class="brand-name">Lumera</span>
    </div>
    <div class="brand-tagline">Body &amp; Health</div>
    <ul class="main-nav">
      <li class="active">Lumera</li>
      <li>Behandlinger</li>
      <li>Produkter</li>
      <li>Priser</li>
      <li>Kontakt</li>
    </ul>
    <div class="social">
      <span class="active"></span><span></span><span></span><span></span>
    </div>
  </aside>

  <main class="hero">
    <div class="hero-photo" role="img" aria-label="Slideshow photo: a therapist's hand guiding a treatment device over a client's stomach in the clinic"></div>
    <h1 class="hero-title">Body &amp;<span class="line-2">Health</span></h1>
    <div class="hero-button">Learn More</div>
    <p class="copyright">© Copyright Lumera 2017</p>
  </main>
</body>
</html>
```